TASMANOVA IT SUPPORT WEBSITE AND CODING

We are a small IT Support company based if Coralbay Western Australia, we need to have our existing website www.tasmanova.com.au converted or redesigned to a format that can be read on iphone , ipad and all browsers, must have facebook like button.

THIS PROJECT IS FOR DESIGN AND CODING OF COMPLETE WEBSITE.

Target Market(s)

Coralbay Local Businesses and Public.

Industry/Entity Type

It Company

Requirements
Must have
• Must be able to be viewed on all mobile devices , iphone , ipad , must have a facebook like button, the logo for tasmanovA is the way tasman ova is written in orange on the current website which is used on all our advertising which needs to stay the same or only change slightly.
Nice to have
• Contact us page that emails us.
Our address on a map.

```html
<!DOCTYPE html>
<html lang="en">
<head>
<meta charset="utf-8">
<title>Tasmanova – IT Support &amp; Computer Specialists</title>
<link href="https://fonts.googleapis.com/css2?family=Barlow:wght@300;400;500;600&family=Nunito:wght@300;400;800&family=Gelasio:ital,wght@1,400&family=Arimo:wght@400;700&display=swap" rel="stylesheet">
<style>
:root{
  --orange:#f07c2c;
  --orange-dark:#d9621a;
  --slate:#5e7385;
  --footer:#4e5f6c;
  --footer-dark:#3e4c57;
  --ink:#222;
  --muted:#555;
  --rule:#dcdcdc;
  --white:#fff;
}
*{box-sizing:border-box;margin:0;padding:0}
html,body{width:1200px;height:987px;overflow:hidden;background:var(--white)}
body{position:relative;font-family:"Arimo",Arial,sans-serif;color:var(--ink)}
.abs{position:absolute}
.brand{left:231px;top:26px;font-family:"Barlow",sans-serif;font-weight:400;font-size:33px;letter-spacing:2px;color:var(--orange)}
.like-box{left:713px;top:33px;display:flex;gap:6px;font-size:10px}
.like-box span{border:1px solid #c9d3e6;background:#eef2f8;padding:2px 6px;color:#3b5998}
.support-btn{left:803px;top:26px;width:172px;height:33px;border:1px solid #ccc;border-radius:3px;background:linear-gradient(#fff,#eee);font-family:"Barlow",sans-serif;font-size:11px;color:#555;display:flex;align-items:center;justify-content:center;letter-spacing:.3px}
.nav{left:0;top:84px;width:1200px;height:47px;background:linear-gradient(#f28a3e,var(--orange-dark));display:flex;padding-left:231px}
.nav a{width:150px;display:flex;align-items:center;justify-content:center;color:var(--white);text-decoration:none;font-family:"Barlow",sans-serif;font-size:14px;border-right:1px solid rgba(0,0,0,.15)}
.nav a.active{background:var(--slate);font-weight:600}
.hero{left:0;top:131px;width:1200px;height:253px;background:linear-gradient(90deg,#8a7866 0%,#4ea5c4 30%,#4ab5cf 55%,#b79b78 80%,#8b9a6a 100%)}
.hero-fade{left:0;top:384px;width:1200px;height:30px;background:linear-gradient(#e6f2f8,#fff)}
.hero-title{left:231px;top:162px;font-family:"Nunito",sans-serif;font-weight:400;color:var(--white);font-size:38px;line-height:42px;text-shadow:0 1px 3px rgba(0,0,0,.3)}
.hero-title b{font-weight:800}
.hero-title .city{font-weight:300}
.hero-art{left:700px;top:150px;width:255px;height:226px;border-radius:18px;background:linear-gradient(160deg,rgba(205,60,50,.55) 0%,rgba(90,130,190,.55) 55%,rgba(170,175,185,.5) 100%)}
.btn{top:310px;height:39px;width:180px;display:flex;align-items:center;gap:14px;padding-left:16px;font-family:"Barlow",sans-serif;font-weight:600;font-size:16px;letter-spacing:.5px;border-radius:2px;box-shadow:0 2px 3px rgba(0,0,0,.3)}
.btn-learn{left:231px;background:linear-gradient(#fbb62a,#f29108);color:#4a2a00}
.btn-contact{left:427px;background:linear-gradient(#fff,#d9d9d9);color:#222}
.h2{font-family:"Barlow",sans-serif;font-size:22px;font-weight:300;color:var(--ink);padding-bottom:6px;border-bottom:1px solid var(--rule)}
.h2 em{font-style:normal;font-weight:600;color:var(--orange)}
.welcome{left:231px;top:428px;width:357px}
.best{left:619px;top:428px;width:356px}
.intro{left:231px;top:478px;width:360px;font-family:"Gelasio",serif;font-style:italic;font-size:10.8px;line-height:19.5px;color:#333}
.badge{left:620px;top:478px;width:91px;height:91px;border:1px solid #ddd;background:#fff;padding:16px}
.badge div{width:100%;height:100%;background:linear-gradient(#e8ebe2,#cfd8c4);border-radius:3px}
.best-copy{left:730px;top:478px;width:245px;font-size:9.5px;line-height:16.5px;color:#555}
.more-btn{display:inline-flex;align-items:center;gap:8px;border:1px solid #ccc;border-radius:3px;background:linear-gradient(#fff,#ececec);color:#333;white-space:nowrap}
.more-lg{left:729px;top:540px;height:28px;padding:0 10px;font-size:10.5px;font-weight:700}
.testimonials{left:237px;top:596px;width:351px}
.news{left:619px;top:596px;width:356px}
.quote{left:231px;width:357px;height:80px}
.quote .avatar{position:absolute;left:2px;top:0;width:66px;height:60px;border:1px solid #ddd;padding:3px}
.quote .avatar div{width:100%;height:100%;background:linear-gradient(#d6b79a,#8f6c55)}
.quote .mark{position:absolute;left:80px;top:2px;font-family:Georgia,serif;font-size:18px;color:#ccc}
.quote p{position:absolute;left:96px;top:7px;width:240px;font-size:9.5px;line-height:16px;color:#222}
.quote small{position:absolute;left:96px;top:44px;font-size:9.5px;color:#888}
.quote small b{color:#555}
.quote-rule{left:231px;width:357px;border-top:1px solid #eee}
.news-item{left:619px;width:356px;height:80px}
.news-item .tick{position:absolute;left:5px;top:4px}
.news-item p{position:absolute;left:25px;top:2px;width:320px;font-size:9.5px;line-height:16px}
.more-sm{position:absolute;left:25px;top:36px;height:20px;padding:0 6px;gap:6px;font-size:8.5px;color:#777}
.footer{left:0;top:823px;width:1200px;height:164px;background:linear-gradient(var(--footer),var(--footer-dark));border-top:3px solid #2f3a42}
.flinks{top:862px;font-size:8.5px;line-height:23px;color:#e8ecef}
.flinks b{color:#fff}
.fdiv{top:860px;height:50px;border-left:1px solid #6c7c88}
.addr{left:708px;top:862px;color:#fff}
.addr h4{font-family:"Barlow",sans-serif;font-size:13px;font-weight:600;letter-spacing:1px;display:flex;gap:8px;align-items:center}
.addr p{margin-top:8px;font-size:8px;line-height:11px;color:#e0e5e9}
.map{left:811px;top:842px;width:134px;height:82px;border:3px solid #e8e8e8;border-radius:3px;background:linear-gradient(120deg,#e9e5d8 55%,#a9c3dd 56%)}
.frule{left:165px;top:940px;width:870px;border-top:1px solid #5f717e}
.copy{left:238px;top:960px;font-size:8px;color:#e8ecef}
.copy b{color:#fff}
.follow{left:825px;top:953px;display:flex;align-items:center;gap:10px;font-size:8.5px;font-weight:700;color:#fff}
.follow i{display:block;width:24px;height:24px;border-radius:3px;background:#8aa0b2}
</style>
</head>
<body>
<header>
  <div class="abs brand">TASMANOVA</div>
  <div class="abs like-box"><span>Like</span><span>303</span></div>
  <div class="abs support-btn">GREAT CUSTOMERS SUPPORT</div>
  <nav class="abs nav">
    <a class="active">HOME</a><a>ABOUT US</a><a>SERVICES</a><a>OUR PRICES</a><a>CONTACT US</a>
  </nav>
</header>

<section>
  <div class="abs hero" role="img" aria-label="Blurred seaside jetty scene with two people walking"></div>
  <div class="abs hero-fade"></div>
  <h1 class="abs hero-title"><b>IT Support &amp;<br>Computer Specialists-</b><br><span class="city">Coralbay</span></h1>
  <div class="abs hero-art" role="img" aria-label="Laptop sheltered under a red umbrella"></div>
  <div class="abs btn btn-learn">
    <svg width="18" height="12" viewBox="0 0 18 12"><path d="M0 6h12M8 2l5 4-5 4M5 2l5 4-5 4" stroke="#4a2a00" stroke-width="2" fill="none"/></svg>LEARN MORE</div>
  <div class="abs btn btn-contact">
    <svg width="18" height="12" viewBox="0 0 18 12"><path d="M0 6h12M8 2l5 4-5 4M5 2l5 4-5 4" stroke="#666" stroke-width="2" fill="none"/></svg>CONTACT US</div>
</section>

<main>
  <h2 class="abs h2 welcome">WELCOME TO <em>OUR SITE</em></h2>
  <p class="abs intro">Lorem ipsum dolor sit amet, consectetur adipiscing elit. In ipsum libero, congue id varius vel, commodo volutpat dolor. Praesent purus nisi, euismod non cursus fermentum, hendrerit quis ante. Integer pulvinar viverra tristique. Vivamus rhoncus feugiat felis id luctus.</p>

  <h2 class="abs h2 best">BEST <em>SERVICE</em></h2>
  <div class="abs badge"><div role="img" aria-label="Certification badge"></div></div>
  <p class="abs best-copy">Lorem ipsum dolor sit amet, consectetur adipiscing elit. In ipsum libero, congue id varius vel, commodo volutpat dolor. Praesent purus nisi, euismod non ...</p>
  <div class="abs more-btn more-lg">Learn More
    <svg width="12" height="12" viewBox="0 0 12 12"><circle cx="6" cy="6" r="6" fill="#bbb"/><path d="M6 3v6M3 6h6" stroke="#fff" stroke-width="1.6"/></svg></div>

  <h2 class="abs h2 testimonials">OUR <em>TESTIMONIALS</em></h2>
  <div class="abs quote" style="top:643px">
    <div class="avatar"><div role="img" aria-label="Customer portrait"></div></div>
    <span class="mark">&ldquo;</span>
    <p>Lorem ipsum dolor sit amet,&nbsp; commodo volutpat dolor. Praesent purus nisi, euismod non ...</p>
    <small>By: <b>delmar</b></small>
  </div>
  <div class="abs quote-rule" style="top:717px"></div>
  <div class="abs quote" style="top:733px">
    <div class="avatar"><div role="img" aria-label="Customer portrait"></div></div>
    <span class="mark">&ldquo;</span>
    <p>Lorem ipsum dolor sit amet,&nbsp; commodo volutpat dolor. Praesent purus nisi, euismod non ...</p>
    <small>By: <b>delmar</b></small>
  </div>

  <h2 class="abs h2 news">LATEST <em>NEWS</em></h2>
  <div class="abs news-item" style="top:648px">
    <svg class="tick" width="12" height="12" viewBox="0 0 12 12"><circle cx="6" cy="6" r="6" fill="#aaa"/><path d="M3 6l2 2 4-4" stroke="#fff" stroke-width="1.6" fill="none"/></svg>
    <p>Lorem ipsum dolor sit amet,&nbsp; commodo volutpat dolor. Praesent purus nisi, euismod non ...</p>
    <div class="more-btn more-sm">Learn More <svg width="9" height="9" viewBox="0 0 12 12"><circle cx="6" cy="6" r="6" fill="#bbb"/><path d="M6 3v6M3 6h6" stroke="#fff" stroke-width="1.6"/></svg></div>
  </div>
  <div class="abs quote-rule" style="left:619px;width:356px;top:717px"></div>
  <div class="abs news-item" style="top:728px">
    <svg class="tick" width="12" height="12" viewBox="0 0 12 12"><circle cx="6" cy="6" r="6" fill="#aaa"/><path d="M3 6l2 2 4-4" stroke="#fff" stroke-width="1.6" fill="none"/></svg>
    <p>Lorem ipsum dolor sit amet,&nbsp; commodo volutpat dolor. Praesent purus nisi, euismod non ...</p>
    <div class="more-btn more-sm">Learn More <svg width="9" height="9" viewBox="0 0 12 12"><circle cx="6" cy="6" r="6" fill="#bbb"/><path d="M6 3v6M3 6h6" stroke="#fff" stroke-width="1.6"/></svg></div>
  </div>
</main>

<footer>
  <div class="abs footer"></div>
  <div class="abs flinks" style="left:231px"><b>Home</b><br>Privacy Policy</div>
  <div class="abs fdiv" style="left:344px"></div>
  <div class="abs flinks" style="left:405px">FAQ's<br>Sitemap</div>
  <div class="abs fdiv" style="left:497px"></div>
  <div class="abs flinks" style="left:558px">Customer Support<br>Contact us</div>
  <div class="abs fdiv" style="left:686px"></div>
  <div class="abs addr">
    <h4>ADDRESS <svg width="22" height="12" viewBox="0 0 22 12"><path d="M1 1l6 5-6 5M9 1l6 5-6 5" stroke="#fff" stroke-width="2.5" fill="none"/></svg></h4>
    <p>47 office, bla bla bla,<br>coralbay australia.</p>
  </div>
  <div class="abs map" role="img" aria-label="Street map showing the office location"></div>
  <div class="abs frule"></div>
  <div class="abs copy">All Right Reserved by <b>Tasmanova.com</b></div>
  <div class="abs follow">Follow us on: <i></i><i></i></div>
</footer>
</body>
</html>
```